Electrical needs letterhead design

Need a letterhead design for an electrical company. Using the same colours as to what are used in the logo.
After a modern design.

Want the logo in top right or top left.

Must include...

ABN 61 842 307 194
PHONE 0492357018
www.voltarnex.com.au
ben@voltarnex.com.au

'ABN' and 'PHONE' in bold.

Keep it basic. Logo top left, details either next to it or far right corner. Dont want any other objects included.

```html
<!DOCTYPE html>
<html lang="en">
<head>
<meta charset="utf-8">
<title>Voltarnex Letterhead</title>
<link rel="stylesheet" href="https://fonts.googleapis.com/css2?family=Crimson+Pro:wght@600;700&family=Open+Sans:wght@400;600&display=swap">
<style>
  :root {
    --backdrop: #4a3128;
    --paper: #ffffff;
    --brand-red: #b3121a;
    --brand-red-bright: #e3171d;
    --brand-red-deep: #8e0c10;
    --swoosh-grey: #5d6a68;
    --footer-ink: #333333;
  }
  * { margin: 0; padding: 0; box-sizing: border-box; }
  html, body {
    width: 954px;
    height: 1200px;
    overflow: hidden;
    background: var(--backdrop);
  }
  .letterhead {
    position: absolute;
    left: 40px;
    top: 33px;
    width: 874px;
    height: 1132px;
    background: var(--paper);
    overflow: hidden;
  }
  .header-band {
    position: absolute;
    left: 0;
    top: 0;
    width: 874px;
    height: 310px;
  }
  .brand-name {
    position: absolute;
    left: 34px;
    top: 86px;
    font-family: "Open Sans", sans-serif;
    font-weight: 400;
    font-size: 50px;
    line-height: 1;
    color: var(--brand-red);
  }
  .contact-details {
    position: absolute;
    right: 32px;
    top: 24px;
    text-align: right;
    font-family: "Crimson Pro", serif;
    color: var(--paper);
    line-height: 1.12;
  }
  .contact-details .phone {
    font-size: 26px;
    font-weight: 600;
    display: flex;
    align-items: center;
    justify-content: flex-end;
    gap: 6px;
  }
  .contact-details .phone svg { width: 18px; height: 18px; }
  .contact-details .abn {
    font-size: 25px;
    font-weight: 700;
    letter-spacing: -0.8px;
  }
  .footer-contacts {
    position: absolute;
    left: 0;
    right: 0;
    bottom: 12px;
    display: flex;
    justify-content: center;
    gap: 22px;
    font-family: "Open Sans", sans-serif;
    font-size: 15px;
    color: var(--footer-ink);
  }
  .footer-contacts .item {
    display: flex;
    align-items: center;
    gap: 8px;
  }
  .footer-contacts svg { width: 15px; height: 15px; }
</style>
</head>
<body>
  <main class="letterhead">
    <svg class="header-band" viewBox="0 0 874 310" aria-hidden="true">
      <defs>
        <linearGradient id="band-red" x1="0" y1="0" x2="1" y2="0">
          <stop offset="0" stop-color="var(--brand-red)"/>
          <stop offset="0.55" stop-color="var(--brand-red-bright)"/>
          <stop offset="1" stop-color="var(--brand-red-deep)"/>
        </linearGradient>
      </defs>
      <path d="M0,2 C520,50 800,140 874,298 V0 H0 Z" fill="var(--swoosh-grey)"/>
      <path d="M0,1 C540,48 800,130 874,244" fill="none" stroke="var(--paper)" stroke-width="5"/>
      <path d="M0,0 H874 V238 C790,128 540,46 0,0 Z" fill="url(#band-red)"/>
    </svg>

    <div class="brand-name">Voltarnex</div>

    <div class="contact-details">
      <div class="phone">
        <svg viewBox="0 0 20 20" aria-label="Phone">
          <circle cx="10" cy="10" r="8.5" fill="none" stroke="currentColor" stroke-width="1.4"/>
          <path d="M7 5.5 C5.5 7 6 10 8 12.5 C10 14.5 12.5 15 14 13.5 L12.5 11.8 L11.2 12.5 C9.8 11.7 8.5 10.2 7.8 8.8 L8.6 7.5 Z" fill="currentColor"/>
        </svg>
        <span>0492357018</span>
      </div>
      <div class="abn">ABN 61 842 307 194</div>
    </div>

    <footer class="footer-contacts">
      <div class="item">
        <svg viewBox="0 0 16 16" aria-label="Email">
          <path d="M1 3 H15 V13 H1 Z" fill="var(--footer-ink)"/>
          <path d="M1 3.5 L8 9 L15 3.5" fill="none" stroke="var(--paper)" stroke-width="1.2"/>
        </svg>
        <span>ben@voltarnex.com.au</span>
      </div>
      <div class="item">
        <svg viewBox="0 0 16 16" aria-label="Website">
          <g fill="none" stroke="var(--footer-ink)" stroke-width="1.2">
            <circle cx="8" cy="8" r="6.5"/>
            <ellipse cx="8" cy="8" rx="3" ry="6.5"/>
            <path d="M1.5 8 H14.5 M2.5 4.8 H13.5 M2.5 11.2 H13.5"/>
          </g>
        </svg>
        <span>www.voltarnex.com.au</span>
      </div>
    </footer>
  </main>
</body>
</html>
```